Harmony Swift Care Business card

We want a business card that matches our business theme. Our website is www.swiftcarehub.example
The company name is Harmony Swift Care
The persons having the business cards will be doctors
My logo is attached.
We have a drive-thru medical center where our motto is Fast, Reliable, and Convenient. Our goal is to change the medical space while utilizing technologies, keeping a professional and clean look

Medical

Info on the card should be: Name, Position, Cell number, website, email address, possibly the office line as well

Requirements
Must have
• Logo
Nice to have
• Professional medical feel with our logo colors incorporated

```html
<!DOCTYPE html>
<html lang="en">
<head>
<meta charset="utf-8">
<title>Harmony Swift Care – Business Card</title>
<link href="https://fonts.googleapis.com/css2?family=Quicksand:wght@500;700&family=Open+Sans:wght@600&display=swap" rel="stylesheet">
<style>
  :root {
    --brand-blue: #1a4496;
    --sky-blue: #3fbde6;
    --card-white: #efeff2;
    --page-grey: #e4e5e9;
    --text-grey: #6e6e72;
    --ink: #1a1a1a;
  }
  * { margin: 0; padding: 0; box-sizing: border-box; }
  html, body {
    width: 1200px; height: 1200px; overflow: hidden;
    background: var(--page-grey);
  }
  .canvas { position: relative; width: 1200px; height: 1200px; }

  .card {
    position: absolute; left: 227px; width: 745px; height: 425px;
    background: var(--card-white);
    border-radius: 38px; overflow: hidden;
    font-family: "Quicksand", sans-serif;
  }
  .card--front { top: 135px; }
  .card--back { top: 640px; }

  .brand { position: absolute; display: flex; align-items: center; }
  .brand__dot {
    flex: none; border-radius: 50%;
    border: solid var(--brand-blue); background: var(--sky-blue);
  }
  .brand__name {
    font-weight: 700; color: var(--brand-blue); line-height: 1.05;
    white-space: nowrap;
  }
  .tagline {
    position: absolute; font-family: "Open Sans", sans-serif; font-weight: 600;
    color: var(--ink); white-space: nowrap; text-align: center;
  }

  .card--front .brand { left: 440px; top: 52px; gap: 14px; }
  .card--front .brand__dot { width: 70px; height: 70px; border-width: 7px; }
  .card--front .brand__name { font-size: 26px; }
  .card--front .tagline { left: 430px; width: 270px; top: 142px; font-size: 13px; }

  .card--back .brand { left: 185px; top: 126px; gap: 22px; }
  .card--back .brand__dot { width: 118px; height: 118px; border-width: 10px; }
  .card--back .brand__name { font-size: 42px; }
  .card--back .tagline { left: 0; right: 0; top: 268px; font-size: 19px; }

  .person__name {
    position: absolute; left: 45px; top: 181px;
    font-size: 26px; font-weight: 700; color: var(--brand-blue);
  }
  .person__role {
    position: absolute; left: 45px; top: 222px;
    font-size: 19px; font-weight: 500; color: var(--text-grey);
  }
  .contact {
    position: absolute; left: 45px; top: 282px; list-style: none;
    font-size: 19px; font-weight: 500; color: var(--text-grey);
  }
  .contact li { display: flex; align-items: center; gap: 8px; height: 26px; }
  .contact svg { width: 17px; height: 17px; flex: none; }
  .website {
    position: absolute; right: 45px; top: 315px;
    font-size: 18px; font-weight: 500; color: var(--text-grey);
  }

  .address-band {
    position: absolute; left: 0; right: 0; top: 358px; height: 41px;
    background: linear-gradient(to right, var(--brand-blue) 0 605px, var(--sky-blue) 605px);
    display: flex; align-items: center; padding-left: 45px;
    font-size: 19px; font-weight: 500; color: #fff;
  }
</style>
</head>
<body>
<div class="canvas">

  <section class="card card--front">
    <div class="brand">
      <div class="brand__name">Harmony Swift<br>Care</div>
      <span class="brand__dot"></span>
    </div>
    <p class="tagline">CARE ON YOUR WAY, EVERY DAY</p>

    <h1 class="person__name">Dorian-Miles K.</h1>
    <p class="person__role">Site Manager</p>

    <ul class="contact">
      <li>
        <svg viewBox="0 0 20 20" aria-hidden="true">
          <circle cx="10" cy="10" r="10" fill="#1a4496"/>
          <path d="M5 8.5c0-2 2.2-3 5-3s5 1 5 3l-1.6.6-.7-1.6c-1.8-.5-3.6-.5-5.4 0l-.7 1.6z M6.5 14.5l1.5-4h4l1.5 4z" fill="#fff"/>
        </svg>
        (555)-014-2830
      </li>
      <li>
        <svg viewBox="0 0 20 20" aria-hidden="true">
          <circle cx="10" cy="10" r="10" fill="#1a4496"/>
          <rect x="5" y="6.5" width="10" height="7" rx="1" fill="none" stroke="#fff" stroke-width="1.3"/>
          <path d="M5.3 7l4.7 3.6L14.7 7" fill="none" stroke="#fff" stroke-width="1.3"/>
        </svg>
        info@swiftcarehub.example
      </li>
    </ul>

    <p class="website">www.swiftcarehub.example</p>

    <div class="address-band">42 Meadowlane Road, Harbor City</div>
  </section>

  <section class="card card--back">
    <div class="brand">
      <div class="brand__name">Harmony Swift<br>Care</div>
      <span class="brand__dot"></span>
    </div>
    <p class="tagline">CARE ON YOUR WAY, EVERY DAY</p>
  </section>

</div>
</body>
</html>
```